Business card Pfotenweide

Business card is for a self-employed dog trainer with own dog school. Name and logo of the dog school are available. Color specifications as well. The design should be classy and minimalist, but also modern. An already existing idea would be: Front: Only the logo Back: Contact data

Font styles to use
Serif
Sans Serif
Other font styles liked:
• Trajan Pro

Colors
f78f20

Requirements
Must have
• Name: Marlene Kessel-Brand Title: Dipl. Dog Trainer Contain my logo Follow my font and color preferences (see files)

```html
<!DOCTYPE html>
<html lang="en">
<head>
<meta charset="utf-8">
<title>Pfotenweide – Business Card</title>
<link href="https://fonts.googleapis.com/css2?family=Cinzel:wght@400;600&family=Libre+Baskerville:wght@700&family=Open+Sans:wght@400;600&display=swap" rel="stylesheet">
<style>
  :root {
    --page-bg: #3a3a3c;
    --card-grey-light: #a3a3a5;
    --card-grey-dark: #6f6f71;
    --brand-orange: #f78f20;
    --brand-orange-deep: #d9741a;
    --paper-white: #f7f7f6;
    --ink-white: #ffffff;
  }
  * { margin: 0; padding: 0; box-sizing: border-box; }
  html, body { width: 1200px; height: 960px; overflow: hidden; }
  body {
    background: var(--page-bg);
    display: flex;
    align-items: center;
    justify-content: center;
    gap: 40px;
  }
  .card {
    position: relative;
    width: 520px;
    height: 300px;
    border-radius: 22px;
    overflow: hidden;
    text-align: center;
  }
  /* Front */
  .card--front {
    background: linear-gradient(180deg, var(--card-grey-light), var(--card-grey-dark));
  }
  .brand {
    position: absolute;
    left: 0; right: 0;
    display: flex;
    flex-direction: column;
    align-items: center;
  }
  .card--front .brand { top: 74px; }
  .brand__dot {
    width: 84px; height: 84px;
    border-radius: 50%;
    background: var(--paper-white);
  }
  .brand__name {
    font-family: "Cinzel", serif;
    font-weight: 600;
    font-size: 34px;
    letter-spacing: 2px;
    line-height: 1;
    margin-top: 10px;
    color: var(--paper-white);
  }
  .brand__url {
    font-family: "Cinzel", serif;
    font-weight: 400;
    font-size: 9px;
    letter-spacing: 4px;
    line-height: 1.2;
    margin-top: 5px;
    color: var(--paper-white);
  }
  /* Back */
  .card--back { background: var(--brand-orange); }
  .card__curve { position: absolute; inset: 0; }
  .card--back .brand { top: 20px; }
  .card--back .brand__dot { width: 70px; height: 70px; background: var(--brand-orange); }
  .card--back .brand__name { font-size: 30px; color: var(--brand-orange-deep); margin-top: 8px; }
  .card--back .brand__url { color: var(--brand-orange-deep); font-size: 8px; }
  .contact {
    position: absolute;
    left: 0; right: 0;
    top: 180px;
    color: var(--ink-white);
  }
  .contact__name {
    font-family: "Libre Baskerville", serif;
    font-weight: 700;
    font-size: 18px;
    line-height: 22px;
  }
  .contact__title {
    font-family: "Libre Baskerville", serif;
    font-weight: 700;
    font-size: 13px;
    line-height: 18px;
  }
  .contact__line {
    font-family: "Open Sans", sans-serif;
    font-weight: 600;
    font-size: 12.5px;
    line-height: 18px;
  }
  .contact__web {
    font-family: "Open Sans", sans-serif;
    font-weight: 600;
    font-size: 13px;
    letter-spacing: 2px;
    line-height: 18px;
  }
</style>
</head>
<body>
  <section class="card card--front" aria-label="Card front">
    <div class="brand">
      <div class="brand__dot"></div>
      <div class="brand__name">PFOTENWEIDE</div>
      <div class="brand__url">WWW.PFOTENWEIDE.CH</div>
    </div>
  </section>

  <section class="card card--back" aria-label="Card back">
    <svg class="card__curve" width="520" height="300" viewBox="0 0 520 300">
      <path d="M0 0 H520 V92 Q300 240 0 105 Z" fill="var(--paper-white)"/>
      <path d="M0 96 Q300 230 520 84" fill="none" stroke="var(--brand-orange)" stroke-width="1.5"/>
    </svg>
    <div class="brand">
      <div class="brand__dot"></div>
      <div class="brand__name">PFOTENWEIDE</div>
      <div class="brand__url">WWW.PFOTENWEIDE.CH</div>
    </div>
    <div class="contact">
      <div class="contact__name">Marlene Kessel-Brand</div>
      <div class="contact__title">Dipl. Dog Trainer</div>
      <div class="contact__line">12 Wiesenstrasse, 8400 Winterthur</div>
      <div class="contact__line">(P) 052 614 3870 &nbsp;(E) marlene@pfotenweide.ch</div>
      <div class="contact__web">www.pfotenweide.ch</div>
    </div>
  </section>
</body>
</html>
```